Fall by my site ads for Facebook

I run an events and exhibition company in Singapore and we are trying to build a presence on Facebook. But my colleagues and I are not very good with web banner and Facebook ad designs so most of our postings are boring and doesn't hit the crowd. So I would like to outsource the design of a series of 3 x banner ad or Facebook posting that creates awareness and bring viewers to my website www.plumtavo.com. Our business is of a B2B nature and our clients are typically well-educated young professionals age 25 to 40 and are social media savvy. They are usually from the Marketing, PR, Communications or Media verticals and typically browse Facebook and Instagram at least once a day.

Target Market(s)

well-educated young professionals age 25 to 40 and are social media savvy. They are usually from the Marketing, PR, Communications or Media verticals and typically browse Facebook and Instagram at least once a day.

Industry/Entity Type

Events

Requirements
Must have
• Our website www.plumtavo.com

```html
<!DOCTYPE html>
<html lang="en">
<head>
<meta charset="utf-8">
<title>Think Big Win The World – Plumtavo</title>
<link rel="stylesheet" href="https://fonts.googleapis.com/css2?family=Montserrat:wght@700;800&display=swap">
<style>
  :root {
    --stage-orange: #ea6a1c;
    --accent-orange: #f0801e;
    --navy-deep: #0c1624;
    --navy-mid: #22364c;
    --steel-blue: #4d6580;
    --sleeve-blue: #6d86a3;
    --skin-warm: #b07a55;
    --skin-light: #d2a27c;
    --headline-white: #ffffff;
  }
  * { margin: 0; padding: 0; box-sizing: border-box; }
  html, body {
    width: 1200px;
    height: 600px;
    overflow: hidden;
  }
  body {
    background: var(--stage-orange);
    position: relative;
    font-family: "Montserrat", sans-serif;
  }
  .banner {
    position: absolute;
    left: 75px;
    top: 108px;
    width: 1050px;
    height: 387px;
    overflow: hidden;
    background: var(--navy-deep);
    box-shadow: 0 6px 14px rgba(0,0,0,0.25);
  }
  .banner__photo {
    position: absolute;
    inset: 0;
    background:
      linear-gradient(180deg, rgba(12,22,36,0) 0%, rgba(12,22,36,0.15) 55%, rgba(12,22,36,0.6) 100%),
      radial-gradient(ellipse 14% 22% at 50% 46%, var(--skin-light), rgba(176,122,85,0) 100%),
      linear-gradient(90deg,
        var(--navy-deep) 0%,
        var(--navy-mid) 22%,
        var(--navy-mid) 30%,
        var(--skin-warm) 40%,
        var(--skin-light) 50%,
        var(--skin-warm) 58%,
        var(--steel-blue) 66%,
        var(--sleeve-blue) 82%,
        var(--steel-blue) 100%);
  }
  .banner__copy {
    position: absolute;
    left: 618px;
    top: 27px;
  }
  .headline {
    color: var(--headline-white);
    font-weight: 800;
    font-size: 94px;
    line-height: 80px;
    letter-spacing: -2px;
    text-transform: uppercase;
    transform: scaleX(0.88);
    transform-origin: left top;
    white-space: nowrap;
    text-shadow: 0 2px 6px rgba(0,0,0,0.25);
  }
  .headline span { display: block; }
  .site-url {
    margin-top: -8px;
    margin-left: 18px;
    color: var(--accent-orange);
    font-weight: 700;
    font-size: 22px;
    line-height: 26px;
    letter-spacing: 1px;
    text-transform: uppercase;
    white-space: nowrap;
  }
</style>
</head>
<body>
  <section class="banner">
    <div class="banner__photo" role="img" aria-label="Photo of two business people in suits shaking hands in front of a dark blue world map"></div>
    <div class="banner__copy">
      <h1 class="headline">
        <span>Think</span>
        <span>Big Win</span>
        <span>The</span>
        <span>World</span>
      </h1>
      <p class="site-url">www.plumtavo.com</p>
    </div>
  </section>
</body>
</html>
```